Flyer for Pharmacy/Medical Convention

Tri-fold flyer for pharmacy/medical convention. The inside of the flyer we would like to look like a venn diagram, possibly using an image similar to our blue logo

Copy write will be submitted when a design is chosen

there will be a flap about educational features, one about supplements an automated recommendations, and a flap about a computer platform to manage patients

Target Market(s)

Pharmacists and Medical Providers

Industry/Entity Type

Supplement

Colors

Designer to choose colors to be used in the design.

Requirements
Must have
• color scheme similar to logos and or label design attached

```html
<!DOCTYPE html>
<html lang="en">
<head>
<meta charset="utf-8">
<title>Convention Tri-fold Flyer – Inside</title>
<link href="https://fonts.googleapis.com/css2?family=Mulish:wght@400;800&display=swap" rel="stylesheet">
<style>
  :root {
    --stage: #2b2b2d;
    --paper: #ffffff;
    --navy: #23388a;
    --blue: #2f4fa4;
    --blue-light: #4f7cc6;
    --red: #e3202a;
    --orange: #f26a2c;
    --ink: #1c1c1f;
    --white: #ffffff;
  }
  html, body {
    margin: 0;
    width: 1200px;
    height: 923px;
    overflow: hidden;
    background: var(--stage);
    font-family: "Mulish", sans-serif;
  }
  .flyer {
    position: absolute;
    left: 67px;
    top: 40px;
    width: 1067px;
    height: 830px;
    overflow: hidden;
    background: var(--paper);
  }
  .flyer-art { position: absolute; inset: 0; }
  .block { position: absolute; text-align: center; color: var(--white); }
  .block p { margin: 0 0 15.8px; font-size: 12.6px; line-height: 15.8px; }
  .heading {
    margin: 0;
    font-size: 18px;
    line-height: 22px;
    font-weight: 400;
    letter-spacing: 0.2px;
  }
  .heading strong { font-weight: 800; }
  .rule {
    display: block;
    width: 100px;
    height: 3px;
    margin: 9px auto 19px;
    background: linear-gradient(90deg, var(--red), var(--orange), var(--red));
  }
  .panel-middle { left: 391px; width: 292px; }
  .panel-right { left: 738px; width: 294px; }
  .educational {
    position: absolute;
    left: 39px;
    top: 381px;
    width: 300px;
    color: var(--ink);
  }
  .educational .heading { color: var(--ink); }
  .educational .rule {
    margin: 4px 0 18px;
    width: 134px;
    height: 2px;
    background: var(--navy);
  }
  .educational p { margin: 0 0 15.8px; font-size: 12.6px; line-height: 15.8px; }
</style>
</head>
<body>
<main class="flyer">
  <svg class="flyer-art" width="1067" height="830" viewBox="0 0 1067 830" aria-hidden="false">
    <defs>
      <linearGradient id="blueFill" x1="0" y1="0" x2="0" y2="1">
        <stop offset="0" stop-color="#3a5fb4"/>
        <stop offset="1" stop-color="#22378a"/>
      </linearGradient>
      <linearGradient id="rightFill" x1="0" y1="0" x2="0" y2="1">
        <stop offset="0" stop-color="#5782c9"/>
        <stop offset="0.5" stop-color="#3558ad"/>
        <stop offset="1" stop-color="#263e92"/>
      </linearGradient>
      <linearGradient id="arcStroke" x1="0" y1="0" x2="0" y2="1">
        <stop offset="0" stop-color="#e3202a"/>
        <stop offset="0.55" stop-color="#e3202a"/>
        <stop offset="1" stop-color="#f26a2c"/>
      </linearGradient>
      <linearGradient id="ringStroke" x1="0" y1="0" x2="1" y2="1">
        <stop offset="0" stop-color="#f26a2c"/>
        <stop offset="1" stop-color="#c81a22"/>
      </linearGradient>
      <linearGradient id="photoTones" x1="0" y1="0" x2="1" y2="1">
        <stop offset="0" stop-color="#e9c79e"/>
        <stop offset="0.5" stop-color="#d99a4e"/>
        <stop offset="1" stop-color="#b9733a"/>
      </linearGradient>
      <linearGradient id="bandFill" x1="0" y1="0" x2="1" y2="0">
        <stop offset="0" stop-color="#23388a"/>
        <stop offset="1" stop-color="#4f7cc6"/>
      </linearGradient>
      <clipPath id="clipRound"><circle cx="507" cy="716" r="116"/></clipPath>
    </defs>

    <rect class="supplements-photo" x="0" y="0" width="620" height="324" fill="url(#photoTones)" role="img" aria-label="Photo of supplement capsules and softgels on wooden spoons with green leaves"/>
    <rect class="photo-band" x="0" y="324" width="560" height="10" fill="url(#bandFill)"/>

    <circle class="venn-circle" cx="835" cy="408" r="514" fill="url(#blueFill)"/>
    <circle class="venn-inner-line" cx="835" cy="408" r="494" fill="none" stroke="#b9bfd0" stroke-width="3"/>
    <circle class="venn-arc" cx="835" cy="408" r="514" fill="none" stroke="url(#arcStroke)" stroke-width="18"/>

    <rect class="panel-right-fill" x="713" y="0" width="354" height="830" fill="url(#rightFill)"/>
    <line x1="713" y1="0" x2="713" y2="830" stroke="#2a418f" stroke-width="1"/>

    <circle cx="507" cy="716" r="126" fill="url(#ringStroke)"/>
    <circle cx="507" cy="716" r="118" fill="#ffffff"/>
    <circle class="classroom-photo" cx="507" cy="716" r="116" fill="#b9a89a" role="img" aria-label="Photo of attendees listening to a presenter in a seminar room"/>

    <path class="clinic-photo-frame" d="M721 830 V700 a30 30 0 0 1 30 -30 H1030 a30 30 0 0 1 30 30 V830 Z" fill="#e3202a"/>
    <path class="clinic-photo" d="M725 830 V702 a27 27 0 0 1 27 -27 H1029 a27 27 0 0 1 27 27 V830 Z" fill="#c9dbe8" role="img" aria-label="Photo of a doctor using a tablet in a hospital ward"/>
  </svg>

  <section class="educational">
    <h2 class="heading"><strong>EDUCATIONAL</strong> FEATURES</h2>
    <span class="rule"></span>
    <p>Lorem ipsum dolor sit amet, consectetuer adipiscing elit, sed diam nonummy nibh euismod tincidunt ut laoreet dolore magna aliquam erat volutpat. Ut wisi enim ad minim veniam, quis nostrud exerci tation ullamcorper suscipit lobortis nisl ut aliquip ex ea commodo consequat. Duis autem vel eum iriure dolor in hendrerit in vulputate velit esse molestie consequat, vel illum dolore eu feugiat nulla facilisis at vero eros et accumsan et iusto odio dignissim qui blandit praesent luptatum zzril delenit augue duis dolore te feugait nulla facilisi.</p>
    <p>Duis autem vel eum iriure dolor in hendrerit in vulputate velit esse molestie consequat, vel illum dolore eu feugiat nulla facilisis at vero eros et accumsan et iusto odio dignissim qui blandit praesent luptatum zzril delenit augue duis dolore te feugait nulla facilisi.</p>
    <p>vero eros et accumsan et iusto odio dignissim qui blandit praesent luptatum zzril delenit augue duis dolore te feugait nulla facilisi.</p>
  </section>

  <section class="block panel-middle" style="top:96px">
    <h2 class="heading"><strong>ABOUT</strong> SUPPLEMENTS</h2>
    <span class="rule" style="margin-bottom:17px"></span>
    <p>Lorem ipsum dolor sit amet, consectetuer adipiscing elit, sed diam nonummy nibh euismod tincidunt ut laoreet dolore magna aliquam erat volutpat. Ut wisi enim ad minim veniam, quis nostrud exerci tation ullamcorper suscipit lobortis nisl ut aliquip ex ea commodo consequat. Duis autem vel eum iriure dolor in hendrerit in vulputate velit esse.</p>
  </section>

  <section class="block panel-middle" style="top:302px">
    <h2 class="heading"><strong>ABOUT</strong> SUPPLEMENTS</h2>
    <span class="rule" style="margin-bottom:17px"></span>
    <p>Lorem ipsum dolor sit amet, consectetuer adipiscing elit, sed diam nonummy nibh euismod tincidunt ut laoreet dolore magna aliquam erat volutpat. Ut wisi enim ad minim veniam, quis nostrud exerci tation ullamcorper suscipit lobortis nisl ut aliquip ex ea commodo consequat. Duis autem vel eum iriure dolor in hendrerit in vulputate velit esse.</p>
    <p>Lorem ipsum dolor sit amet, consectetuer adipiscing elit, sed diam nonummy nibh euismod tincidunt ut laoreet dolore magna aliquam erat volutpat.</p>
  </section>

  <section class="block panel-right" style="top:96px">
    <h2 class="heading"><strong>AUTOMATED</strong> RECOMMENDATIONS</h2>
    <span class="rule" style="margin-bottom:11px"></span>
    <p>Lorem ipsum dolor sit amet, consectetuer adipiscing elit, sed diam nonummy nibh euismod tincidunt ut laoreet dolore magna aliquam erat volutpat. Ut wisi enim ad minim veniam, quis nostrud exerci tation ullamcorper suscipit lobortis nisl ut aliquip ex ea commodo consequat. Duis autem vel eum iriure dolor in hendrerit in vulputate velit esse.</p>
    <p>Ut wisi enim ad minim veniam, quis nostrud exerci tation ullamcorper suscipit lobortis nisl ut aliquip ex ea commodo consequat. Duis autem vel eum iriure dolor in hendrerit in vulputate velit esse.</p>
  </section>

  <section class="block panel-right" style="top:366px">
    <h2 class="heading"><strong>COMPUTER PLATFORM</strong> TO<br>MANAGE PATIENTS</h2>
    <span class="rule" style="margin-bottom:11px"></span>
    <p>Lorem ipsum dolor sit amet, consectetuer adipiscing elit, sed diam nonummy nibh euismod tincidunt ut laoreet dolore magna aliquam erat volutpat. Ut wisi enim ad minim veniam, quis nostrud exerci tation ullamcorper suscipit lobortis nisl ut aliquip ex ea commodo consequat. Duis autem vel eum iriure dolor in hendrerit in vulputate velit esse.</p>
    <p>Ut wisi enim ad minim veniam, quis nostrud exerci tation ullamcorper suscipit lobortis nisl ut aliquip ex ea commodo consequat. Duis autem vel eum iriure dolor in hendrerit in vulputate velit esse.</p>
  </section>
</main>
</body>
</html>
```